Business consultant needs a new powerpoint design

Design a fresh new powerpoint template for a consultant. The powerpoint design needs to include our company logo which I have attached and the colours & feel of the template used should be consistent with the logo design
Target Market(s)
Employees of large corporate companies
Industry/Entity Type
Business Consultant
Look and feel

```html
<!DOCTYPE html>
<html lang="en">
<head>
<meta charset="utf-8">
<title>Northway Consulting – Slide Template</title>
<link rel="stylesheet" href="https://fonts.googleapis.com/css2?family=Open+Sans:wght@400;600;700&display=swap">
<style>
  :root {
    --brand-blue: #2fa3dc;
    --brand-blue-dark: #1f8fc9;
    --brand-grey: #6f7377;
    --text-dark: #4a4d50;
    --text-muted: #8a8d90;
    --page-bg: #e9e9e9;
    --slide-white: #ffffff;
    --rule: #d6d8da;
  }
  * { box-sizing: border-box; margin: 0; padding: 0; }
  html, body {
    width: 849px; height: 1200px; overflow: hidden;
    background: var(--page-bg);
    font-family: "Open Sans", Arial, sans-serif;
  }
  .canvas { position: relative; width: 849px; height: 1200px; }
  .slide {
    position: absolute; left: 51px; width: 747px;
    box-shadow: 0 4px 14px rgba(0,0,0,.25);
    overflow: hidden;
  }

  /* Title slide */
  .slide--title { top: 34px; height: 532px; background: var(--brand-blue); }
  .title-decor { position: absolute; left: 30px; top: 20px; }
  .brand-lockup {
    position: absolute; right: 44px; top: 200px;
    display: flex; align-items: center; gap: 10px; color: #fff;
  }
  .brand-lockup__dot { width: 52px; height: 52px; border-radius: 50%; background: #fff; flex: none; }
  .brand-lockup__name { font-size: 34px; font-weight: 700; line-height: 1; letter-spacing: 0.5px; white-space: nowrap; }
  .brand-lockup__sub { font-size: 9px; font-weight: 700; letter-spacing: 2px; text-transform: uppercase; margin-top: 5px; white-space: nowrap; }
  .slogan {
    position: absolute; left: 220px; right: 40px; top: 318px; color: #fff; text-align: right;
  }
  .slogan__heading { font-size: 24px; font-weight: 400; margin-bottom: 8px; }
  .slogan__body { font-size: 13px; line-height: 1.5; }

  /* Content slide */
  .slide--content { top: 600px; height: 566px; background: var(--slide-white); }
  .content-title { position: absolute; left: 34px; top: 26px; font-size: 27px; font-weight: 700; color: var(--brand-blue); }
  .content-subtitle { position: absolute; left: 34px; top: 66px; font-size: 15px; color: var(--text-muted); }
  .pillars { position: absolute; left: 70px; right: 40px; top: 160px; }
  .pillar { display: flex; align-items: center; height: 58px; margin-bottom: 42px; }
  .pillar__tag {
    width: 176px; height: 54px; flex: none; display: flex; align-items: center; justify-content: center;
    color: #fff; font-size: 17px; font-weight: 600;
    clip-path: polygon(0 0, 86% 0, 100% 50%, 86% 100%, 0 100%);
    padding-right: 18px;
  }
  .pillar__tag--blue { background: var(--brand-blue); }
  .pillar__tag--grey { background: var(--brand-grey); }
  .pillar__text { margin-left: 24px; font-size: 12px; line-height: 1.5; color: var(--text-dark); text-align: justify; }
  .content-footer {
    position: absolute; left: 0; right: 0; bottom: 0; height: 58px;
    border-top: 1px solid var(--rule); display: flex; align-items: center; justify-content: space-between;
    padding: 0 24px;
  }
  .footer-brand { display: flex; align-items: center; gap: 6px; color: var(--brand-blue); font-weight: 700; font-size: 18px; }
  .footer-brand__dot { width: 18px; height: 18px; border-radius: 50%; background: var(--brand-blue); }
  .pager { font-size: 11px; color: var(--text-muted); display: flex; gap: 8px; align-items: center; }
  .pager__btn { display: inline-block; width: 14px; height: 14px; background: var(--rule); border-radius: 2px; }
  .footer-url { font-size: 11px; color: var(--text-muted); }
</style>
</head>
<body>
<div class="canvas">

  <section class="slide slide--title">
    <svg class="title-decor" width="230" height="230" viewBox="0 0 230 230" aria-hidden="true">
      <circle cx="115" cy="115" r="112" fill="#ffffff" fill-opacity="0.12"/>
    </svg>
    <div class="brand-lockup">
      <div class="brand-lockup__dot"></div>
      <div>
        <div class="brand-lockup__name">NORTHWAY</div>
        <div class="brand-lockup__sub">Business Consulting</div>
      </div>
    </div>
    <div class="slogan">
      <h1 class="slogan__heading">Add your presentation Slogan here</h1>
      <p class="slogan__body">I need to be able to update the deck as feedback on the course is received. The content of the slide deck is completed this is purely about</p>
    </div>
  </section>

  <section class="slide slide--content">
    <h2 class="content-title">Mission, Vision &amp; Goal</h2>
    <p class="content-subtitle">Put your great sub title here</p>
    <div class="pillars">
      <div class="pillar">
        <div class="pillar__tag pillar__tag--blue">Mission</div>
        <p class="pillar__text">What we need is a template (or master) which can be varied by ourselves from case to case. Most of our cases are colorful and it's important to transport the passion of transport the passion by ourselves from case to</p>
      </div>
      <div class="pillar">
        <div class="pillar__tag pillar__tag--grey">Vision</div>
        <p class="pillar__text">What we need is a template (or master) which can be varied by ourselves from case to case. Most of our cases are colorful and it's important to transport the passion of transport the passion by ourselves from case to</p>
      </div>
      <div class="pillar">
        <div class="pillar__tag pillar__tag--blue">Goal</div>
        <p class="pillar__text">What we need is a template (or master) which can be varied by ourselves from case to case. Most of our cases are colorful and it's important to transport the passion of transport the passion by ourselves from case to</p>
      </div>
    </div>
    <footer class="content-footer">
      <div class="footer-brand"><span class="footer-brand__dot"></span>NORTHWAY</div>
      <div class="pager"><span class="pager__btn"></span>2 of 9<span class="pager__btn"></span></div>
      <div class="footer-url">www.northwayconsult.com</div>
    </footer>
  </section>

</div>
</body>
</html>
```